Playing Card Box Deisgn

Quick video of what we're looking for in this design:

https://clip.tovermaze.com/watch/p3KQRw82tnYdLmcx7ZbuHe?

Here's our company website:
https://ourbrandoquel.com/

Attached is the file of what we have so far for this box design. Feel free to add or make other design suggestions

```html
<!DOCTYPE html>
<html lang="en">
<head>
<meta charset="utf-8">
<title>Brandoquel Playing Cards – Box Dieline</title>
<link rel="stylesheet" href="https://fonts.googleapis.com/css2?family=Cormorant+Garamond:wght@500;600&family=Jost:ital,wght@0,500;1,400&family=Montserrat:wght@800&display=swap">
<style>
  :root {
    --page: #ffffff;
    --board: #231f20;
    --cut: #d98ac0;
    --gold: #f08a24;
    --ink: #ffffff;
    --suit-red: #e8262b;
    --suit-orange: #f47a2a;
    --suit-purple: #8a4fa3;
    --suit-blue: #3f6fb6;
    --suit-yellow: #f6c21c;
    --suit-pink: #e8398e;
    --suit-green: #7bbf44;
    --suit-teal: #4bbf99;
  }
  html, body {
    margin: 0;
    width: 848px;
    height: 1200px;
    overflow: hidden;
    background: var(--page);
  }
  .canvas {
    width: 848px;
    height: 1200px;
    display: flex;
    align-items: center;
    justify-content: center;
  }
  .dieline { display: block; }
  .cut-line { fill: none; stroke: var(--cut); stroke-width: 1.2; }
  .frame { fill: none; stroke: var(--gold); stroke-width: 3; }
  .frame-thin { fill: none; stroke: var(--gold); stroke-width: 1.6; }
  .frame-dotted { fill: none; stroke: var(--gold); stroke-width: 1.6; stroke-dasharray: 2 4; }
  .spine-url {
    font-family: "Jost", sans-serif;
    font-weight: 500;
    font-size: 15px;
    letter-spacing: 2px;
    fill: var(--ink);
  }
  .brand-spaced {
    font-family: "Cormorant Garamond", serif;
    font-weight: 500;
    font-size: 20px;
    letter-spacing: 9px;
    fill: var(--ink);
  }
  .back-url {
    font-family: "Jost", sans-serif;
    font-weight: 500;
    font-size: 10px;
    letter-spacing: 2px;
    fill: var(--ink);
  }
  .back-copy {
    margin: 0;
    font-family: "Jost", sans-serif;
    font-style: italic;
    font-weight: 400;
    font-size: 14.2px;
    line-height: 15.6px;
    color: var(--ink);
    text-align: justify;
    text-align-last: center;
    hyphens: manual;
  }
  .front-title {
    font-family: "Cormorant Garamond", serif;
    font-weight: 600;
    font-size: 64px;
    fill: var(--ink);
  }
  .front-subtitle {
    font-family: "Montserrat", sans-serif;
    font-weight: 800;
    font-size: 29px;
    letter-spacing: -1.5px;
    fill: var(--ink);
  }
  .edition-pill { fill: var(--gold); }
  .edition-label {
    font-family: "Cormorant Garamond", serif;
    font-weight: 600;
    font-size: 17px;
    fill: var(--board);
  }
</style>
</head>
<body>
<main class="canvas">
  <svg class="dieline" width="800" height="706" viewBox="256 36 1066 941" xmlns="http://www.w3.org/2000/svg">
    <defs>
      <linearGradient id="suit-row" x1="0" x2="1" y1="0" y2="0">
        <stop offset="0" stop-color="var(--suit-red)"/>
        <stop offset="0.35" stop-color="var(--suit-green)"/>
        <stop offset="0.65" stop-color="var(--suit-yellow)"/>
        <stop offset="1" stop-color="var(--suit-purple)"/>
      </linearGradient>
      <linearGradient id="suit-emblem" x1="0" x2="1" y1="0" y2="1">
        <stop offset="0" stop-color="#6a4a8c"/>
        <stop offset="0.35" stop-color="#b8373a"/>
        <stop offset="0.7" stop-color="#c48a2a"/>
        <stop offset="1" stop-color="#3f8a62"/>
      </linearGradient>
    </defs>

    <!-- board -->
    <rect class="board" x="256" y="36" width="1066" height="941" fill="var(--board)"/>

    <!-- cut lines -->
    <g class="cut-lines">
      <path class="cut-line" d="M436 263 H1240 V751 H337 V263 H436"/>
      <line class="cut-line" x1="436" y1="263" x2="436" y2="751"/>
      <line class="cut-line" x1="789" y1="263" x2="789" y2="751"/>
      <line class="cut-line" x1="887" y1="263" x2="887" y2="751"/>
      <path class="cut-line" d="M436 263 V165 H789 V263 M436 165 V140 Q436 70 612 70 Q789 70 789 140 V165"/>
      <path class="cut-line" d="M337 263 V181 H412 L420 228 L436 245"/>
      <path class="cut-line" d="M887 263 V181 H812 L804 228 L789 245"/>
      <path class="cut-line" d="M337 751 V833 H412 L420 786 L436 769"/>
      <path class="cut-line" d="M887 751 V833 H812 L804 786 L789 769"/>
      <path class="cut-line" d="M887 751 V850 H1240 V751 M887 850 V875 Q887 950 1063 950 Q1240 950 1240 875 V850"/>
      <path class="cut-line" d="M1240 263 L1314 290 V730 L1240 751"/>
    </g>

    <!-- top tuck band -->
    <g class="tuck-band">
      <rect class="frame" x="449" y="177" width="327" height="72"/>
      <rect class="frame-thin" x="459" y="187" width="307" height="52"/>
      <rect x="536" y="204" width="155" height="18" fill="url(#suit-row)" opacity="0.85" role="img" aria-label="Row of four small coloured card suit icons"/>
    </g>

    <!-- left spine -->
    <g class="spine spine-left">
      <rect class="frame" x="354" y="279" width="66" height="457"/>
      <rect class="frame-thin" x="364" y="330" width="46" height="355" rx="4"/>
      <text class="spine-url" transform="translate(380 507) rotate(90)" text-anchor="middle">WWW.OURBRANDOQUEL.COM</text>
    </g>

    <!-- back panel -->
    <g class="panel panel-back">
      <rect class="frame" x="447" y="277" width="329" height="463"/>
      <rect class="frame-thin" x="458" y="290" width="307" height="438"/>
      <circle cx="612" cy="368" r="7" fill="var(--gold)"/>
      <text class="brand-spaced" x="616" y="420" text-anchor="middle">BRANDOQUEL</text>
      <foreignObject x="481" y="459" width="263" height="165">
        <p xmlns="http://www.w3.org/1999/xhtml" class="back-copy">Our patented design is lightyears ahead of the competition. This sleek design means flawless performance and no downtime (We have less than 1% service calls, which means these are truly built to last.) Brandoquel is the most customizable system available, allowing users to design one-of-a-kind sequences of up to 250 unique color/brightness combinations at a time.</p>
      </foreignObject>
      <text class="back-url" x="612" y="713" text-anchor="middle">WWW.OURBRANDOQUEL.COM</text>
    </g>

    <!-- right spine -->
    <g class="spine spine-right">
      <rect class="frame" x="805" y="279" width="67" height="457"/>
      <rect class="frame-thin" x="815" y="330" width="47" height="355" rx="4"/>
      <text class="spine-url" transform="translate(843 507) rotate(-90)" text-anchor="middle">WWW.OURBRANDOQUEL.COM</text>
    </g>

    <!-- front panel -->
    <g class="panel panel-front">
      <path class="frame" d="M898 280 H1004 Q1012 312 1063 312 Q1114 312 1122 280 H1228 V742 H898 Z"/>
      <rect class="frame-dotted" x="907" y="289" width="313" height="445"/>
      <path class="frame-thin" d="M1004 268 Q1012 300 1063 300 Q1114 300 1122 268"/>
      <text class="front-title" x="1063" y="392" text-anchor="middle" textLength="255" lengthAdjust="spacingAndGlyphs">BRANDOQUEL</text>
      <polygon class="frame" points="985,410 1140,410 1172,442 1172,604 1140,636 985,636 953,604 953,442"/>
      <polygon points="990,418 1135,418 1164,447 1164,599 1135,628 990,628 961,599 961,447" fill="url(#suit-emblem)" opacity="0.55" role="img" aria-label="Four coloured card suits – heart, spade, diamond and club – arranged around a white crossed X"/>
      <text class="front-subtitle" x="1061" y="700" text-anchor="middle">PLAYING CARDS</text>
      <rect class="edition-pill" x="1003" y="719" width="117" height="26" rx="13"/>
      <text class="edition-label" x="1061" y="738" text-anchor="middle">STANDARD</text>
    </g>

    <!-- bottom tuck band -->
    <g class="tuck-band">
      <rect class="frame" x="900" y="764" width="326" height="72"/>
      <rect class="frame-thin" x="910" y="774" width="306" height="52"/>
      <rect x="987" y="791" width="155" height="18" fill="url(#suit-row)" opacity="0.85" role="img" aria-label="Row of four small coloured card suit icons"/>
    </g>
  </svg>
</main>
</body>
</html>
```